Website Redesign

I am looking to have our website redone. We recently paid to have this done and are very unhappy with the results. We're looking to have a much more modern and clean feeling while GREATLY enhancing the user experience. We are very close to have a new logo designed as well as having some brand colors (Pantone 3005C). We want our site to have a human feel to it without focusing completely on our products. That being said, we need our products to play a more prominent role as our current site doesn't very clearly display what we do.
Our website: lumvaro-seating.com
Websites we like (overall feel): jorvex.com, daltonrigg.com
Websites we like (functionality): brimfold.com
I apologize, we are new to ArtQuorum. I am showing a budget of $500 for this project. I know we'd go beyond that. I do not believe that we'll be able to overhaul our website for $500. I apologize for any confusion.

```html
<!DOCTYPE html>
<html lang="en">
<head>
<meta charset="utf-8">
<title>Lumvaro Seating</title>
<link href="https://fonts.googleapis.com/css2?family=Oswald:wght@300;400&family=Open+Sans:wght@400;600&display=swap" rel="stylesheet">
<style>
:root{
  --blue:#1b9be0;
  --ink:#333;
  --muted:#555;
  --soft:#888;
  --band:#f1f1f1;
  --tile:#f2f2f2;
  --line:#dcdcdc;
  --page-bg:#f6f6f6;
}
*{box-sizing:border-box;margin:0;padding:0}
html,body{width:1200px;height:1072px;overflow:hidden}
body{background:var(--page-bg);font-family:"Open Sans",Arial,sans-serif;color:var(--ink);position:relative}
.topbar{position:absolute;left:0;top:0;width:1200px;height:4px;background:#2a2a2a}
.page{position:absolute;left:14px;top:4px;width:1169px;height:1068px;background:#fff;box-shadow:0 0 6px rgba(0,0,0,.12)}
.header{position:absolute;left:0;top:0;width:1169px;height:119px;background:linear-gradient(#fff,#f4f4f4)}
.brand{position:absolute;left:38px;top:38px;display:flex;align-items:center;gap:8px;font-family:"Oswald",sans-serif;font-weight:400;font-size:30px;color:#2b2b2b}
.brand-dot{width:10px;height:10px;border-radius:50%;background:var(--blue)}
.drawer-tab{position:absolute;left:1126px;top:-4px;width:31px;height:21px;background:var(--blue);border-radius:0 0 3px 3px}
.nav{position:absolute;top:0;left:0;height:119px;width:1169px}
.nav a{position:absolute;top:62px;transform:translateX(-50%);font-family:"Oswald",sans-serif;font-size:16px;color:#222;text-decoration:none;letter-spacing:.2px}
.nav .active-bg{position:absolute;left:526px;top:46px;width:77px;height:73px;background:linear-gradient(#fff,#f0f0f0);border-bottom:4px solid var(--blue)}
.hero{position:absolute;left:0;top:119px;width:1169px;height:503px;background:linear-gradient(90deg,#e9e6e2 0%,#d9d3cc 45%,#cfc6bc 70%,#3a3532 78%,#e6e0da 90%,#2a2624 100%)}
.hero-caption{position:absolute;left:106px;top:78px;width:468px;height:193px;background:rgba(238,236,233,.85);padding:20px 32px}
.hero-caption h1{font-family:"Oswald",sans-serif;font-weight:400;font-size:29px;color:#3a3a3a;margin-bottom:12px}
.hero-caption p{font-family:"Oswald",sans-serif;font-weight:300;font-size:17px;line-height:26px;color:#333}
.hero-arrow{position:absolute;top:218px;width:36px;height:36px}
.features{position:absolute;left:0;top:627px;width:1169px;height:169px;background:var(--band);border-top:1px solid #e4e4e4;border-bottom:1px solid #e4e4e4}
.feature{position:absolute;top:48px;width:250px}
.feature svg{position:absolute;left:0;top:0}
.feature h3{margin-left:40px;font-family:"Oswald",sans-serif;font-weight:400;font-size:20px;color:#222}
.feature p{margin-left:40px;margin-top:10px;font-size:13.5px;line-height:24px;color:var(--muted)}
.divider{position:absolute;top:50px;width:1px;height:105px;background:var(--line)}
.info{position:absolute;top:822px}
.info h2{font-family:"Oswald",sans-serif;font-weight:400;font-size:20px;color:#222;margin-bottom:12px}
.photo{width:334px;height:130px;border:6px solid #e2e2e2}
.info p{margin-top:12px;font-size:15px;line-height:25px;color:#444;width:350px}
.specialty{display:flex;flex-direction:column;gap:12px}
.spec-item{display:flex;width:341px;height:57px;background:var(--tile)}
.spec-icon{width:57px;height:57px;display:flex;align-items:center;justify-content:center;background:#e6e6e6}
.spec-item.highlight .spec-icon{background:var(--blue)}
.spec-text{padding:8px 0 0 22px}
.spec-text strong{display:block;font-weight:600;font-size:15px;color:#222}
.spec-text span{font-size:13.5px;color:var(--soft)}
</style>
</head>
<body>
<div class="topbar"></div>
<div class="page">
  <header class="header">
    <div class="brand"><span>Lumvaro</span><span class="brand-dot"></span></div>
    <nav class="nav">
      <div class="active-bg"></div>
      <a style="left:565px">HOME</a>
      <a style="left:691px">PRODUCTS</a>
      <a style="left:831px">ORDERING</a>
      <a style="left:968px">COMPANY</a>
      <a style="left:1101px">CONTACT</a>
    </nav>
  </header>
  <div class="drawer-tab">
    <svg width="31" height="21" viewBox="0 0 31 21"><path d="M11 10l4.5 4 4.5-4" fill="none" stroke="#fff" stroke-width="1.6"/></svg>
  </div>

  <section class="hero" role="img" aria-label="Woman in a dark jacket standing at a round café table in a bright office">
    <div class="hero-caption">
      <h1>Welcome to Lumvaro Space</h1>
      <p>The last thing we think about when we’re creating new products, or refining old ones, is furniture. Because at Lumvaro Seating, furniture is designed for people. So we start with them.</p>
    </div>
    <svg class="hero-arrow" style="left:38px" viewBox="0 0 36 36"><circle cx="18" cy="18" r="18" fill="rgba(0,0,0,.28)"/><path d="M25 18H11M17 11l-7 7 7 7" fill="none" stroke="#fff" stroke-width="3"/></svg>
    <svg class="hero-arrow" style="left:1109px" viewBox="0 0 36 36"><circle cx="18" cy="18" r="18" fill="rgba(0,0,0,.28)"/><path d="M11 18h14M19 11l7 7-7 7" fill="none" stroke="#fff" stroke-width="3"/></svg>
  </section>

  <section class="features">
    <div class="feature" style="left:36px">
      <svg width="28" height="32" viewBox="0 0 28 32"><rect x="2" y="4" width="24" height="4" rx="2" fill="#111"/><path d="M14 8v10M14 18l-8 12M14 18l8 12" stroke="#111" stroke-width="3"/></svg>
      <h3>LV Tables</h3>
      <p>Lumvaro Seating warrants that its products shall be free from defects....</p>
    </div>
    <div class="divider" style="left:291px"></div>
    <div class="feature" style="left:314px">
      <svg width="28" height="34" viewBox="0 0 28 34"><rect x="6" y="2" width="16" height="14" rx="6" fill="#111"/><rect x="3" y="16" width="22" height="4" fill="#111"/><path d="M6 20v12M22 20v12" stroke="#111" stroke-width="3"/></svg>
      <h3>LV Seating</h3>
      <p>We’ve noticed that a lot of people like to sit down apparently.</p>
    </div>
    <div class="divider" style="left:569px"></div>
    <div class="feature" style="left:592px">
      <svg width="28" height="36" viewBox="0 0 28 36"><path d="M3 3h22l-4 7H7z" fill="#111"/><rect x="10" y="10" width="8" height="20" fill="#111"/><rect x="4" y="30" width="20" height="4" fill="#111"/></svg>
      <h3>LV Lecterns</h3>
      <p>Any person who’s ever stood behind a lectern will tell you they’ve never given a second.</p>
    </div>
    <div class="divider" style="left:846px"></div>
    <div class="feature" style="left:869px;width:270px">
      <svg width="40" height="40" viewBox="0 0 40 40"><rect x="4" y="4" width="24" height="28" rx="4" fill="none" stroke="#111" stroke-width="3"/><path d="M9 9v18M14 9v18M19 9v18M24 9v18" stroke="#111" stroke-width="2"/><path d="M2 34h30" stroke="#111" stroke-width="2"/><circle cx="8" cy="37" r="2.5" fill="#111"/><circle cx="28" cy="37" r="2.5" fill="#111"/></svg>
      <h3 style="margin-left:62px">Transport Solutions</h3>
      <p style="margin-left:62px">People expect furniture that’s designed to be portable, stackable.</p>
    </div>
  </section>

  <section class="info" style="left:37px">
    <h2>About Lumvaro Seating</h2>
    <div class="photo" role="img" aria-label="Bright office with white meeting tables and black swivel chairs" style="background:linear-gradient(180deg,#dad8d2,#c9c1b4 60%,#8f8478)"></div>
    <p>We manufacture products that are designed to be moved, it helps that we’re nimble.</p>
  </section>
  <section class="info" style="left:413px">
    <h2>Why Choose Us</h2>
    <div class="photo" role="img" aria-label="Close-up of a hand typing on a white keyboard" style="background:linear-gradient(135deg,#f0f0f0,#d4d7da 50%,#e8d2c4)"></div>
    <p>Many of the products we’ve made are direct results through collaboration with people.</p>
  </section>
  <section class="info" style="left:788px">
    <h2>Our Sepcialty</h2>
    <div class="specialty">
      <div class="spec-item highlight">
        <div class="spec-icon"><svg width="34" height="34" viewBox="0 0 34 34"><circle cx="17" cy="17" r="16" fill="#fff"/><path d="M11 23v-7M15 23v-10M19 23v-8M23 23v-12" stroke="#777" stroke-width="3"/></svg></div>
        <div class="spec-text"><strong>Good Reputation</strong><span>Lorem Ipsum dummy text always</span></div>
      </div>
      <div class="spec-item">
        <div class="spec-icon"><svg width="34" height="34" viewBox="0 0 34 34"><circle cx="17" cy="17" r="16" fill="#fff"/><circle cx="17" cy="18" r="8" fill="none" stroke="#444" stroke-width="1.6"/><path d="M17 13v5l3 2M10 10l3-2M24 10l-3-2" stroke="#444" stroke-width="1.6" fill="none"/></svg></div>
        <div class="spec-text"><strong>On-time Delivery</strong><span>Lorem Ipsum dummy text always</span></div>
      </div>
      <div class="spec-item">
        <div class="spec-icon"><svg width="34" height="34" viewBox="0 0 34 34"><circle cx="17" cy="17" r="16" fill="#fff"/><ellipse cx="17" cy="15" rx="9" ry="6" fill="#aaa"/><path d="M14 20l-2 5 6-4z" fill="#aaa"/></svg></div>
        <div class="spec-text"><strong>Professional Behavior</strong><span>Lorem Ipsum dummy text always</span></div>
      </div>
    </div>
  </section>
</div>
</body>
</html>
```